Business Card Design

RETAIL HIGH END CONTEMPORARY WOMEN'S CLOTHING STORE
MODERN, SIMPLE, CLEAN, COOL

WE ARE ALL ABOUT NY and CALIF STYLE.... CLASSY but EDGY..
COOLEST DENIM , Trendsetting, NEUTRAL Pallettes,
Collections : Fig and Stone, Dorian Vesk, PMW, K47, QTB
Don't need names of collections on card. thats just good info
for designer of card.

WOULD LIKE THE FONT TO BE INTERESTING, but CLEAN
We are on facebook daily with photos of outfits we put together
which you can look up and friend us.... MolvaHarbor
Also on instagram .
Open to options on color and size, but need cool and fresh.

Contact Information for Business Card

DELLA 5417 Larkmoor Rd. #309 Ember Court Arcade..Va. Beach, Va. 23987
Phone 757.386.5049 Fax 757.386-2613 EMAIL..DELLAMODE@QUILLBOX.COM

```html
<!DOCTYPE html>
<html lang="en">
<head>
<meta charset="utf-8">
<title>MolvaHarbor Business Card</title>
<link rel="stylesheet" href="https://fonts.googleapis.com/css2?family=Baloo+2:wght@600;700&family=Pathway+Gothic+One&display=swap">
<style>
  :root {
    --bg-top: #ffffff;
    --bg-bottom: #5cffa6;
    --brand-green: #3bb873;
    --address-green: #5fe895;
    --phone-green: #86f5b2;
    --email-green: #36b26f;
  }
  html, body {
    margin: 0;
    padding: 0;
    overflow: hidden;
  }
  .card {
    position: relative;
    width: 1200px;
    height: 702px;
    overflow: hidden;
    background: linear-gradient(to bottom, var(--bg-top) 0%, #c9ffe0 30%, var(--bg-bottom) 100%);
    font-family: "Baloo 2", sans-serif;
  }
  .brand-name {
    position: absolute;
    left: 0;
    top: 0;
    width: 1200px;
    height: 702px;
  }
  .brand-name text {
    font-family: "Baloo 2", sans-serif;
    font-weight: 700;
    font-size: 124px;
    fill: var(--brand-green);
  }
  .address {
    position: absolute;
    left: 206px;
    top: 256px;
    margin: 0;
    font-weight: 600;
    font-size: 44px;
    line-height: 55px;
    color: var(--address-green);
    letter-spacing: 0.5px;
  }
  .address span { display: block; }
  .numbers {
    position: absolute;
    left: 206px;
    top: 482px;
    margin: 0;
    white-space: nowrap;
    color: var(--phone-green);
  }
  .phone {
    font-family: "Pathway Gothic One", sans-serif;
    font-size: 88px;
    line-height: 90px;
  }
  .fax {
    font-family: "Baloo 2", sans-serif;
    font-weight: 600;
    font-size: 44px;
    margin-left: 18px;
  }
  .email {
    position: absolute;
    left: 206px;
    top: 578px;
    margin: 0;
    font-weight: 600;
    font-size: 45px;
    line-height: 50px;
    color: var(--email-green);
    white-space: nowrap;
  }
</style>
</head>
<body>
  <div class="card">
    <svg class="brand-name" viewBox="0 0 1200 702" aria-label="MolvaHarbor">
      <text transform="translate(186 619) rotate(-90)" textLength="551" lengthAdjust="spacingAndGlyphs">MolvaHarbor</text>
    </svg>
    <p class="address">
      <span>DELLA 5417 Larkmoor</span>
      <span>Rd. #309 Ember Court</span>
      <span>Arcade..Va.</span>
      <span>Beach, Va. 23987</span>
    </p>
    <p class="numbers">
      <span class="phone">Phone 757.386.5049</span><span class="fax">Fax 757.386-2613</span>
    </p>
    <p class="email">EMAIL..DELLAMODE@QUILLBOX.COM</p>
  </div>
</body>
</html>
```